Coffee Roastery Label Sticker Design

We are starting a small Micro-Coffee-Roastery and are looking for a catchy design, which might look a bit hipster style, but not too much. It's called "lantern roastery", because we started roasting first in our backyard / garden by our house.
At the end of the logo and the details of the sticker (like all text elements) we need to be able to modify later by ourselfs. Coffee type, origin of coffee and so one ...
The label will be sticked on a white craftpaper coffee bag of 250grams. Sticker size around 8x12.5 cm.
The coffee bag should be an eye-catcher in a shop-shelve compared to the other coffee brands.
Another example that i really like (just to get you another idea of what we would love to get because we really like that style): https://pixvaultcdn.net/art_img/5172839/80412/61937204/qhrmzvle7k4b9x2d6wf1ny3u8p_image.png).
OR https://packfolioweb.net/blog/2016/3/14/ember-beans?

Target Market(s)

"0Speciality Coffee" lovers
High quality specialty coffee and a clear origin of the bean and fair trade or project coffee is what makes our roasted coffee product special

Logo Text

Laterne Rösterei

Requirements
Must have
• A house and a garden with either flowers or a tree is what we have in mind.
The printed label will be square 8x12.5 cm. We will use the logo on the printed label (we will print on our own printer) and on a homepage.
Nice to have
• In the attached logo example, there is no connection to a coffee business. Actually it would be a nice detail to include somehow either a descent coffee bean, a cup or a tiny roastery machine or whatever is in your mind with coffee ... (not a grinder)
Black and white is OK, but we also like colourfull very much
Please see the attached documents with sample designs that we created on our own with canvas. It's not too bad, but also a bit boring. If you have a completely different idea, please go for it. we are very open for other cool and hip designs or also quite descent and femail touch is fine too, but no must.

```html
<!DOCTYPE html>
<html lang="de">
<head>
<meta charset="utf-8">
<title>Laterne Rösterei – Etikett</title>
<link rel="stylesheet" href="https://fonts.googleapis.com/css2?family=Pathway+Gothic+One&family=Allura&family=Arimo&display=swap">
<style>
  :root {
    --page: #ffffff;
    --page-edge: #d6d6d6;
    --label-cream: #fdfdc8;
    --ink: #111111;
    --roof-peach: #f9c796;
    --roof-pink: #f59494;
    --grass: #9acd6a;
  }
  html, body {
    margin: 0;
    width: 1200px;
    height: 920px;
    overflow: hidden;
    background: var(--page);
  }
  .canvas {
    position: relative;
    width: 1198px;
    height: 918px;
    border: 1px solid var(--page-edge);
    background: var(--page);
  }
  .label {
    position: absolute;
    left: 348px;
    top: 62px;
    width: 503px;
    height: 798px;
    background: var(--label-cream);
  }
  .label__frame {
    position: absolute;
    left: 13px;
    top: 12px;
    width: 471px;
    height: 765px;
    border: 4px solid var(--ink);
  }
  .label__house {
    position: absolute;
    left: 69px;
    top: 55px;
    width: 366px;
    height: 162px;
  }
  .label__brand {
    position: absolute;
    left: 0;
    width: 100%;
    top: 232px;
    margin: 0;
    text-align: center;
    white-space: nowrap;
    font-family: "Pathway Gothic One", sans-serif;
    font-weight: 400;
    font-size: 74px;
    line-height: 1;
    letter-spacing: 3px;
    color: var(--ink);
  }
  .label__garden {
    position: absolute;
    left: 38px;
    top: 330px;
    width: 424px;
    height: 80px;
  }
  .label__tagline {
    position: absolute;
    left: 0;
    width: 100%;
    top: 428px;
    text-align: center;
    white-space: nowrap;
    font-family: "Allura", cursive;
    font-size: 46px;
    line-height: 1.2;
    color: var(--ink);
  }
  .label__rule {
    position: absolute;
    height: 0;
    border-top: 1.5px solid var(--ink);
  }
  .label__rule--top { left: 38px; width: 422px; top: 509px; }
  .label__rule--bottom { left: 40px; width: 424px; top: 614px; }
  .label__product {
    position: absolute;
    left: 0;
    width: 100%;
    top: 531px;
    text-align: center;
    font-family: "Arimo", sans-serif;
    font-size: 21px;
    line-height: 31px;
    color: var(--ink);
  }
  .label__details {
    position: absolute;
    right: 30px;
    top: 664px;
    text-align: right;
    font-family: "Arimo", sans-serif;
    font-size: 13.5px;
    line-height: 18.5px;
    color: var(--ink);
    margin: 0;
    padding: 0;
    list-style: none;
  }
</style>
</head>
<body>
<div class="canvas">
  <section class="label">
    <div class="label__frame"></div>

    <svg class="label__house" role="img" aria-label="Illustration: Hausdach mit Kamin und zwei Giebelfenstern" viewBox="0 0 366 162">
      <defs>
        <linearGradient id="roofTone" x1="0" y1="0" x2="0" y2="1">
          <stop offset="0" stop-color="#f7b4a0"/>
          <stop offset="1" stop-color="#f9c796"/>
        </linearGradient>
      </defs>
      <rect x="0" y="0" width="366" height="162" fill="url(#roofTone)"/>
    </svg>

    <h1 class="label__brand">Laterne Rösterei</h1>

    <svg class="label__garden" role="img" aria-label="Illustration: Gartenwiese mit Gräsern und Blumen" viewBox="0 0 424 80">
      <rect x="0" y="0" width="424" height="80" fill="var(--grass)"/>
    </svg>

    <div class="label__tagline">Speciality Coffee</div>

    <div class="label__rule label__rule--top"></div>
    <div class="label__product">FILTERKAFFEE<br>ÄTHIOPIEN - GUJI</div>
    <div class="label__rule label__rule--bottom"></div>

    <ul class="label__details">
      <li>250 GRAMM</li>
      <li>HELLE RÖSTUNG</li>
      <li>KAFFEE AUS ÄTHIOPIEN</li>
      <li>100% ARABICA | WASHED</li>
      <li>GERÖSTET IN 6250 LINDENAU</li>
      <li>WWW.LATERNE-ROESTEREI.CH</li>
    </ul>
  </section>
</div>
</body>
</html>
```